Packaging design for an cardboard box / carton for modern Scandinavian cushion covers

The design should be made on a finished pattern for a cardboard box / carton. Ideally, the design can be directly on a packaging manufacturer. The box should measure 250 x 180 x 50 mm. Skanidnavian packaging design for modern cushion covers with classic patterns. The color design of the packaging should be kept simple and not too overloaded. 10 euros on a cushion cover.

Target Market(s)

End customer / retail

Requirements
Must have
• The logo (see appendix) should be included as well as a cut-out through which the customer can see the pattern of the product.
Nice to have
• Please attach the German texts (see appendix) to the draft.

```html
<!DOCTYPE html>
<html lang="de">
<head>
<meta charset="utf-8">
<title>Faltschachtel Kissenbezug</title>
<link rel="stylesheet" href="https://fonts.googleapis.com/css2?family=Source+Sans+3:wght@400;600&display=swap">
<style>
  :root {
    --paper: #ffffff;
    --brand-blue: #25a8c9;
    --die-line: #9a9a9a;
    --ink: #1a1a1a;
    --name-ink: #3b3b3b;
    --pattern-grey: #a9a9a9;
    --pattern-light: #d4d4d4;
  }
  html, body {
    margin: 0;
    padding: 0;
    width: 1200px;
    height: 940px;
    overflow: hidden;
    background: var(--paper);
  }
  .canvas {
    position: relative;
    width: 870px;
    height: 680px;
    transform: scale(1.3793, 1.3824);
    transform-origin: 0 0;
    font-family: "Source Sans 3", "Myriad Pro", sans-serif;
    color: var(--ink);
  }
  .dieline {
    position: absolute;
    inset: 0;
  }
  .dieline .cut { fill: var(--paper); stroke: var(--die-line); stroke-width: 0.7; }
  .dieline .panel-frame { fill: none; stroke: var(--brand-blue); stroke-width: 7; }

  .back-copy {
    position: absolute;
    left: 86px;
    top: 206px;
    width: 218px;
    font-size: 10.3px;
    line-height: 16.3px;
    text-align: justify;
    margin: 0;
  }
  .back-copy p { margin: 0 0 13px; }

  .spine-url {
    position: absolute;
    width: 240px;
    top: 338px;
    font-size: 18px;
    color: var(--brand-blue);
    text-align: center;
    transform: translate(-50%, -50%) rotate(-90deg);
    white-space: nowrap;
  }
  .spine-url--left { left: 392px; }
  .spine-url--right { left: 790px; }

  .product-window {
    position: absolute;
    left: 483px;
    top: 165px;
    width: 215px;
    height: 218px;
    border-radius: 15px;
    background: radial-gradient(circle at 50% 50%, var(--pattern-light), var(--pattern-grey));
  }
  .product-title {
    position: absolute;
    left: 440px;
    width: 304px;
    top: 401px;
    text-align: center;
    font-size: 13px;
    color: var(--brand-blue);
    margin: 0;
  }
  .product-specs {
    position: absolute;
    left: 440px;
    width: 304px;
    top: 424px;
    text-align: center;
    font-size: 10px;
    margin: 0;
  }
  .shop-name {
    position: absolute;
    top: 472px;
    transform: translateX(-50%);
    white-space: nowrap;
    font-size: 13px;
    font-weight: 600;
    color: var(--name-ink);
  }
  .shop-name--back { left: 196px; }
  .shop-name--front { left: 592px; }
</style>
</head>
<body>
<div class="canvas">
  <svg class="dieline" width="870" height="680" viewBox="0 0 870 680" aria-hidden="true">
    <polygon class="cut" points="40,122 40,78 50,35 335,35 345,78 345,122"/>
    <polygon class="cut" points="40,553 40,600 50,643 335,643 345,600 345,553"/>
    <polygon class="cut" points="350,122 350,80 356,35 430,35 436,80 436,122"/>
    <polygon class="cut" points="350,553 350,598 356,640 430,640 436,598 436,553"/>
    <polygon class="cut" points="439,122 439,78 449,35 735,35 745,78 745,122"/>
    <polygon class="cut" points="439,553 439,600 449,643 735,643 745,600 745,553"/>
    <polygon class="cut" points="749,122 749,80 755,35 828,35 834,80 834,122"/>
    <polygon class="cut" points="749,553 749,598 755,640 828,640 834,598 834,553"/>
    <rect class="cut" x="348" y="122" width="89" height="431"/>
    <rect class="cut" x="747" y="122" width="88" height="431"/>
    <rect class="panel-frame" x="41.5" y="125.5" width="303" height="424"/>
    <rect class="panel-frame" x="440.5" y="125.5" width="303" height="424"/>
  </svg>

  <div class="back-copy">
    <p>Mit diesem Kissenbezug erwerben Sie nicht nur einen Hingucker der Ihrem Sofa den letzten Hauch Gemütlichkeit und Stil verpasst, sondern entscheiden sich auch für 100% Qualität und Langlebigkeit.</p>
    <p>Unsere Kissenebzüge bestehen aus 100% Leinen bzw. Baumwolle und wurden von unseren sorgfältig ausgewählten Partnern nachhaltig hergestellt.</p>
  </div>

  <div class="shop-name shop-name--back">fjordtextil.de</div>

  <div class="spine-url spine-url--left">fjordtextil.de</div>

  <div class="product-window" role="img" aria-label="Sichtfenster auf das grau-weiße skandinavische Rautenmuster des Kissenbezugs"></div>
  <p class="product-title">Gemütlichkeit im Skandinavischen Stil</p>
  <p class="product-specs">45 x45 cm | 100 % Leinen | Mit Reissverschluss</p>

  <div class="shop-name shop-name--front">fjordtextil.de</div>

  <div class="spine-url spine-url--right">fjordtextil.de</div>
</div>
</body>
</html>
```